OLU58 biz card & Stationery

LU58 is a personalized shopping experience brought to you, that lets you find and discover fashion goods through a collection of boutiques curated by taste-makers - celebrities, stylists, designers, and fashion bloggers. Boutiques uses visual technology to help fashionistas discover and shop their look and creates the opportunity for designers to showcase their collections and latest inspirations online.

OLU58 is built on technology developed by our team of fashion experts who work with engineers to “teach” our computer systems to understand various patterns, pairings, and genre definitions. When signed into your account, OLU58 learns about your style and preferences and in turn, provides you better results and recommendations over time. Ultimately, OLU58 will provide shoppers with a much richer and interactive shopping experience and help drive traffic to retailers' websites.

We need a definitely cool business card. The card must be black! And must use our official logo which can be download from OLU58.com

The address for Letter head and evenlop, please use 4872 Crestwick Parkway, Sutie 510 Los Angeles CA90412, email will be anyone@OLU58.com, website is www.OLU58.com

thanks

We received some of the design, thanks. But most of the design are not what we want. We need a very clean version with black ground, you may also use some dark gray to add the element. please take a look at http://morvalstudio.no/work/#pelter__ostrama/, we do like this kind of design very much. hope it help.

```html
<!DOCTYPE html>
<html lang="en">
<head>
<meta charset="utf-8">
<title>OLU58 Letterhead</title>
<link rel="stylesheet" href="https://fonts.googleapis.com/css2?family=Arimo&family=Barlow:wght@300&display=swap">
<style>
  :root {
    --canvas: #ffffff;
    --ink-black: #222222;
    --band-light: #4a4a4a;
    --band-dark: #232323;
    --paper: #ffffff;
    --name-white: #ffffff;
    --tagline-grey: #9a9a9a;
    --contact-grey: #d8d8d8;
    --watermark: #e8e8e8;
    --label-grey: #6a6a6a;
    --shadow: rgba(0, 0, 0, 0.16);
  }
  html, body {
    margin: 0;
    padding: 0;
    overflow: hidden;
  }
  .canvas {
    position: relative;
    width: 1200px;
    height: 900px;
    background: var(--canvas);
    overflow: hidden;
  }
  .sheet {
    position: absolute;
    top: 113px;
    width: 477px;
    height: 674px;
    background: var(--ink-black);
  }
  .sheet--main { left: 62px; }
  .sheet--other { left: 661px; }
  .paper {
    position: absolute;
    right: 0;
    bottom: 0;
    left: 18px;
    background: var(--paper);
    border-top-left-radius: 20px;
    box-shadow: 4px 4px 8px var(--shadow);
  }
  .sheet--main .paper { top: 97px; }
  .sheet--other .paper { top: 22px; left: 19px; }

  .brand {
    position: absolute;
    left: 28px;
    top: 22px;
    font-family: "Arimo", sans-serif;
  }
  .brand__name {
    display: block;
    font-size: 34px;
    line-height: 38px;
    letter-spacing: 1px;
    color: var(--name-white);
  }
  .brand__tagline {
    display: block;
    margin-top: 8px;
    font-size: 8px;
    letter-spacing: 0.8px;
    color: var(--tagline-grey);
  }
  .contact-band {
    position: absolute;
    left: 166px;
    top: 23px;
    width: 282px;
    height: 55px;
    border-top-left-radius: 10px;
    background: linear-gradient(90deg, var(--band-dark) 0%, var(--band-light) 22%, #333333 65%, var(--band-dark) 100%);
  }
  .contact {
    position: absolute;
    left: 22px;
    top: 12px;
    margin: 0;
    font-family: "Arimo", sans-serif;
    font-style: normal;
    font-size: 6.3px;
    line-height: 8px;
    color: var(--contact-grey);
  }
  .watermark {
    position: absolute;
    left: 0;
    right: 0;
    top: 262px;
    text-align: center;
    font-family: "Arimo", sans-serif;
    color: var(--watermark);
  }
  .watermark__name {
    display: block;
    font-size: 78px;
    line-height: 80px;
    letter-spacing: 2px;
  }
  .watermark__tagline {
    display: block;
    margin-top: 14px;
    font-size: 17px;
    letter-spacing: 1.5px;
  }
  .caption {
    position: absolute;
    top: 823px;
    margin: 0;
    width: 200px;
    text-align: center;
    font-family: "Barlow", sans-serif;
    font-weight: 300;
    font-size: 15px;
    line-height: 18px;
    letter-spacing: 0.5px;
    color: var(--label-grey);
  }
  .caption--main { left: 201px; }
  .caption--other { left: 800px; }
</style>
</head>
<body>
<main class="canvas">
  <section class="sheet sheet--main" aria-label="Letterhead main page">
    <div class="brand">
      <span class="brand__name">OLU58</span>
      <span class="brand__tagline">CURATED STYLE ONLINE</span>
    </div>
    <div class="contact-band">
      <address class="contact">
        4872 Crestwick Parkway, Sutie 510<br>
        Los Angeles CA90412<br>
        anyone@OLU58.com<br>
        www.OLU58.com
      </address>
    </div>
    <div class="paper"></div>
  </section>

  <section class="sheet sheet--other" aria-label="Letterhead other pages">
    <div class="paper">
      <div class="watermark">
        <span class="watermark__name">OLU58</span>
        <span class="watermark__tagline">CURATED STYLE ONLINE</span>
      </div>
    </div>
  </section>

  <p class="caption caption--main">Main Page</p>
  <p class="caption caption--other">Other Pages</p>
</main>
</body>
</html>
```